Business Card Design for Funky New Cloud Security Start-up

We're looking for kick ass business cards to make use stand out from the crowd in a world that's dominated by dull, boring, blue logos.

We have a logo (designed here on make forge) and we'd like to build on the brand theme of "Security made simple."

Please use following details for sample:

Peter Holmsby
CEO
+61 (0)4127 568 213
pete@varqel.com

2708/46 Tamberly Street
Sydney NSW 2000
Australia

Target Market(s)

Customers will be large enterprise clients - typically VP level. Also resellers of our product who are mid-tier.

Industry/Entity Type

Business

Font styles to use
Sans Serif

Requirements
Must have
• Use the colour scheme from the attached logo
Do not put space for a fax - it's old school
Easy to use on quill press
Use a font that complements the logo font

```html
<!DOCTYPE html>
<html lang="en">
<head>
<meta charset="utf-8">
<title>varqel business card</title>
<link rel="stylesheet" href="https://fonts.googleapis.com/css2?family=Quicksand:wght@400;500;700&display=swap">
<style>
  :root {
    --backdrop: #e4e5e6;
    --card: #f4f4f2;
    --band: #82b5d0;
    --brand: #3f8fbf;
    --ink: #5a5d61;
    --on-band: #ffffff;
    --shadow: rgba(0, 0, 0, 0.16);
  }
  * { box-sizing: border-box; margin: 0; padding: 0; }
  html, body {
    width: 1200px;
    height: 873px;
    overflow: hidden;
    background: var(--backdrop);
    font-family: "Quicksand", sans-serif;
  }
  .sheet {
    position: relative;
    width: 1200px;
    height: 873px;
    display: flex;
    align-items: center;
    justify-content: center;
    gap: 60px;
  }
  .card {
    position: relative;
    width: 520px;
    height: 316px;
    background: var(--card);
    box-shadow: 0 6px 18px var(--shadow);
    overflow: hidden;
  }
  .card__art {
    position: absolute;
    inset: 0;
    width: 100%;
    height: 100%;
  }
  .band { fill: var(--band); }
  .rule { stroke: var(--band); stroke-width: 6; }

  /* front */
  .address {
    position: absolute;
    left: 30px;
    top: 34px;
    color: var(--on-band);
    font-size: 15px;
    line-height: 1.45;
    font-weight: 500;
    font-style: normal;
  }
  .person {
    position: absolute;
    left: 262px;
    top: 28px;
    color: var(--ink);
  }
  .person__name {
    font-size: 25px;
    font-weight: 700;
    letter-spacing: 0.5px;
  }
  .person__title {
    margin-top: 8px;
    margin-left: 58px;
    font-size: 15px;
    font-weight: 500;
  }
  .contact {
    position: absolute;
    left: 30px;
    bottom: 30px;
    color: var(--on-band);
    font-size: 15px;
    line-height: 1.55;
    font-weight: 500;
    list-style: none;
  }
  .brand {
    position: absolute;
    display: flex;
    align-items: center;
    gap: 10px;
    color: var(--brand);
    font-weight: 700;
    line-height: 1;
  }
  .brand__dot {
    display: block;
    border-radius: 50%;
    background: var(--brand);
  }
  .brand--front {
    right: 34px;
    bottom: 92px;
    font-size: 36px;
  }
  .brand--front .brand__dot { width: 14px; height: 14px; }

  /* back */
  .brand--back {
    left: 0;
    right: 0;
    top: 138px;
    justify-content: center;
    font-size: 40px;
  }
  .brand--back .brand__dot { width: 16px; height: 16px; }
</style>
</head>
<body>
<main class="sheet">

  <section class="card card--front" aria-label="Card front">
    <svg class="card__art" viewBox="0 0 520 316" aria-hidden="true">
      <polygon class="band" points="0,0 218,0 362,316 0,316"/>
    </svg>
    <address class="address">
      2708/46 Tamberly Street<br>
      Sydney NSW 2000<br>
      Australia
    </address>
    <div class="person">
      <h1 class="person__name">Peter Holmsby</h1>
      <p class="person__title">CEO</p>
    </div>
    <ul class="contact">
      <li>+61 (0)4127 568 213</li>
      <li>pete@varqel.com</li>
    </ul>
    <div class="brand brand--front">
      <span class="brand__dot"></span>
      <span class="brand__name">varqel</span>
    </div>
  </section>

  <section class="card card--back" aria-label="Card back">
    <svg class="card__art" viewBox="0 0 520 316" aria-hidden="true">
      <line class="rule" x1="30" y1="62" x2="520" y2="62"/>
      <line class="rule" x1="0" y1="266" x2="490" y2="266"/>
    </svg>
    <div class="brand brand--back">
      <span class="brand__dot"></span>
      <span class="brand__name">varqel</span>
    </div>
  </section>

</main>
</body>
</html>
```